Packaging Design Project

My company produces chocolate bars; currently have 4 bars that are packaged in slim window boxes.

I need some product images, but the photos we've taken look awful. I think someone with solid Photoshop skills could take our electronic files and create some product images based on the digital files.

I need 4 product images. Also, if you are able to product any additional general images like this:
http://snapvelle.com/brivantcocoafan/cocoa-makes-our-recess/

```html
<!DOCTYPE html>
<html lang="en">
<head>
<meta charset="utf-8">
<title>Odette Cacao – Dark Chocolate Bars</title>
<link rel="stylesheet" href="https://fonts.googleapis.com/css2?family=Architects+Daughter&display=swap">
<style>
  :root {
    --page: #fdf8e8;
    --box: #0b0b0b;
    --box-edge: #2a2a2a;
    --ink: #f2f2f2;
    --ink-soft: #cfcfcf;
    --band-cherry: #ff2b2b;
    --band-chili: #a5161b;
    --band-nibs: #1f80ff;
    --band-salt: #93d4e2;
    --band-salt-ink: #1f4d8a;
    --choc-dark: #1a0d0a;
    --choc-mid: #3b1d16;
  }
  * { box-sizing: border-box; margin: 0; padding: 0; }
  html, body { width: 1200px; height: 644px; overflow: hidden; }
  body {
    background: var(--page);
    font-family: "Architects Daughter", cursive;
    position: relative;
  }
  .bar-box {
    position: absolute;
    width: 145px;
    height: 335px;
    background: linear-gradient(180deg, #1b1b1b 0%, var(--box) 18%, var(--box) 100%);
    border: 1px solid var(--box-edge);
    box-shadow: 0 8px 14px rgba(0,0,0,0.18);
    color: var(--ink);
    text-align: center;
  }
  .bar-box--cherry { left: 117px; top: 185px; }
  .bar-box--chili  { left: 383px; top: 135px; }
  .bar-box--nibs   { left: 648px; top: 185px; }
  .bar-box--salt   { left: 914px; top: 135px; }

  .brand-name {
    position: absolute;
    top: 14px; left: 0; right: 0;
    font-size: 17px;
    line-height: 1.05;
    letter-spacing: 1.5px;
    color: var(--ink);
  }
  .flavour-band {
    position: absolute;
    top: 75px; left: 0; right: 0;
    height: 21px;
    font-size: 13px;
    line-height: 21px;
    color: var(--ink);
    white-space: nowrap;
  }
  .bar-box--cherry .flavour-band { background: var(--band-cherry); font-size: 11.5px; }
  .bar-box--chili  .flavour-band { background: var(--band-chili); }
  .bar-box--nibs   .flavour-band { background: var(--band-nibs); }
  .bar-box--salt   .flavour-band { background: var(--band-salt); color: var(--band-salt-ink); }

  .product-line {
    position: absolute;
    top: 112px; left: 0; right: 0;
    font-size: 11.5px;
    line-height: 15px;
    color: var(--ink);
  }
  .bar-window {
    position: absolute;
    top: 158px; left: 28px;
    width: 90px; height: 78px;
    border: 1px solid #3a3a3a;
    background: linear-gradient(135deg, var(--choc-mid) 0%, var(--choc-dark) 60%, #0a0504 100%);
  }
  .description {
    position: absolute;
    top: 246px; left: 14px; right: 14px;
    font-size: 10px;
    line-height: 12.5px;
    color: var(--ink-soft);
  }
  .net-weight {
    position: absolute;
    bottom: 10px; left: 0; right: 0;
    font-size: 7px;
    color: var(--ink-soft);
    letter-spacing: 0.5px;
  }
</style>
</head>
<body>
  <main class="product-lineup">
    <article class="bar-box bar-box--cherry">
      <p class="brand-name">ODETTE<br>CACAO</p>
      <p class="flavour-band">Vanilla Bean &amp; Cherries</p>
      <p class="product-line">Fine Belgian<br>Dark Chocolate</p>
      <div class="bar-window" role="img" aria-label="Dark chocolate bar with pink cherry flecks seen through the window"></div>
      <p class="description">56% Belgian dark chocolate with vanilla bean &amp; dried cherries</p>
      <p class="net-weight">NET WT 1.8 OZ (50g)</p>
    </article>

    <article class="bar-box bar-box--chili">
      <p class="brand-name">ODETTE<br>CACAO</p>
      <p class="flavour-band">Chili Pepper</p>
      <p class="product-line">Fine Belgian<br>Dark Chocolate</p>
      <div class="bar-window" role="img" aria-label="Dark chocolate bar with red chili flecks seen through the window"></div>
      <p class="description">56% Belgian dark chocolate with organic chili pepper</p>
      <p class="net-weight">NET WT 1.8 OZ (50g)</p>
    </article>

    <article class="bar-box bar-box--nibs">
      <p class="brand-name">ODETTE<br>CACAO</p>
      <p class="flavour-band">Cocoa Nibs</p>
      <p class="product-line">Fine Belgian<br>Dark Chocolate</p>
      <div class="bar-window" role="img" aria-label="Dark chocolate bar with white drizzle seen through the window"></div>
      <p class="description">56% Belgian dark chocolate with roasted cocoa nibs</p>
      <p class="net-weight">NET WT 1.8 OZ (50g)</p>
    </article>

    <article class="bar-box bar-box--salt">
      <p class="brand-name">ODETTE<br>CACAO</p>
      <p class="flavour-band">Fleur de Sel</p>
      <p class="product-line">Fine Belgian<br>Dark Chocolate</p>
      <div class="bar-window" role="img" aria-label="Dark chocolate bar with pale blue sea salt crystals seen through the window"></div>
      <p class="description">56% Belgian dark chocolate with handharvested French sea salt</p>
      <p class="net-weight">NET WT 1.8 OZ (50g)</p>
    </article>
  </main>
</body>
</html>
```